Plakat-Design für Wirtschafts- und Kaufmannsring
Zielgruppe
Der Wirtschafts- und Kaufmannsring ist ein Verein - Zusammenschluss von Gewerbetreibenden. Im Prinzip wie die Organisation Ring der Werkstattmeister.
Aufgabenstellung
An den Ortseingängen der Gemeinde Lindenmoos stehen Ortsinformationstafeln welche immer für den Aufzug von aktuellen Veranstaltungen genutzt werden. Dies sind quasi Stahlträger auf welche Plakate aufgezogen werden. Bisher wurden diese immer wieder abgebaut und aufgebaut. Ziel ist es jetzt, dass die das ganze Jahr über stehen - was nicht so schön aussieht. Deswegen soll hier quasi ein Plakat aufgezogen werden, welches genutzt wird, wenn keine Veranstaltung ansteht.
Auf dem Plakat soll zu sehen sein:
- Logo Gemeinde Lindenmoos
- Logo WKR Lindenmoos
- Webseite www.wkr-lindenmoos.de und von der Gemeinde www.lindenmoos-ort.de
- Slogan 'Ein starkes Team' gerne sind wir auch für weitere Ideen offen
Informationen von der Firma welche den Druck ausführt
Die Schilder sind 110cm x 160cm, wenn sie das auf einer Plane(Banner) haben wollen, kommen noch 8 Ösen rein, 2cm vom Rand. Die Grafik sollte am besten auf Originalgröße angelegt werden und abspeichern als PDF.

```html
<!DOCTYPE html>
<html lang="de">
<head>
<meta charset="utf-8">
<title>Ein starkes Team – WKR Lindenmoos</title>
<link rel="stylesheet" href="https://fonts.googleapis.com/css2?family=Roboto+Slab:wght@500;700&display=swap">
<style>
  :root {
    --stage: #141418;
    --night-violet: #352a62;
    --teal: #4bb8b0;
    --ochre: #c98b23;
    --lime: #c3c41f;
    --orange: #ec7b38;
    --slogan-edge: #2a2050;
    --paper: #ffffff;
    --brick: #a7382a;
    --town-grey: #9b9b9b;
  }
  * { margin: 0; padding: 0; box-sizing: border-box; }
  html, body {
    width: 1200px; height: 900px; overflow: hidden;
    background: var(--stage);
    font-family: "Roboto Slab", Georgia, serif;
  }
  .poster {
    position: absolute; left: 295px; top: 20px;
    width: 610px; height: 860px;
    background: var(--paper);
    display: flex; flex-direction: column;
  }
  .poster-stage {
    position: relative;
    height: 707px;
    background: var(--night-violet);
    overflow: hidden;
  }
  .hands-illustration {
    position: absolute; left: 0; top: 150px;
    width: 100%; height: 557px;
  }
  .municipality-mark {
    position: absolute; left: 50%; top: 14px;
    transform: translateX(-50%);
    display: flex; flex-direction: column; align-items: center; gap: 8px;
    color: var(--paper);
    font-weight: 500; font-size: 17px; text-align: center; line-height: 1.2;
  }
  .municipality-mark .mark-dot {
    width: 74px; height: 74px; border-radius: 50%;
    background: var(--paper);
  }
  .slogan {
    position: absolute; right: 48px; top: 415px;
    text-align: right;
    color: var(--teal);
    font-weight: 700; font-size: 78px; line-height: 84px;
    letter-spacing: 1px;
    text-shadow: 3px 3px 0 var(--slogan-edge);
  }
  .poster-footer {
    flex: 1;
    position: relative;
    padding: 10px 10px 0;
  }
  .club-mark {
    display: flex; align-items: center; gap: 10px;
    height: 62px; padding-left: 4px;
  }
  .club-mark .mark-dot {
    width: 54px; height: 54px; border-radius: 50%;
    background: var(--brick);
  }
  .club-mark .club-name {
    color: var(--brick);
    font-weight: 700; font-size: 22px; letter-spacing: 0.5px;
  }
  .town-band {
    display: block; width: 100%; height: 36px; margin-top: -8px;
  }
  .web-links {
    display: flex; justify-content: space-between;
    padding: 8px 22px 0;
    color: var(--brick);
    font-weight: 500; font-size: 18px; letter-spacing: 0.6px;
  }
</style>
</head>
<body>
  <main class="poster">
    <section class="poster-stage">
      <svg class="hands-illustration" role="img" aria-label="Illustration: bunte erhobene Hände in Türkis, Ocker, Limette und Orange mit Jubelstrichen" viewBox="0 0 610 557" preserveAspectRatio="none">
        <defs>
          <linearGradient id="handTones" x1="0" y1="0" x2="1" y2="0">
            <stop offset="0" stop-color="#4bb8b0"/>
            <stop offset="0.35" stop-color="#c98b23"/>
            <stop offset="0.62" stop-color="#c3c41f"/>
            <stop offset="1" stop-color="#ec7b38"/>
          </linearGradient>
          <linearGradient id="fadeUp" x1="0" y1="0" x2="0" y2="1">
            <stop offset="0" stop-color="#352a62" stop-opacity="1"/>
            <stop offset="0.55" stop-color="#352a62" stop-opacity="0.35"/>
            <stop offset="1" stop-color="#352a62" stop-opacity="0.1"/>
          </linearGradient>
        </defs>
        <rect width="610" height="557" fill="url(#handTones)"/>
        <rect width="610" height="557" fill="url(#fadeUp)"/>
      </svg>

      <div class="municipality-mark">
        <span class="mark-dot"></span>
        <span class="municipality-name">Gemeinde Lindenmoos</span>
      </div>

      <h1 class="slogan">Ein<br>starkes<br>Team</h1>
    </section>

    <footer class="poster-footer">
      <div class="club-mark">
        <span class="mark-dot"></span>
        <span class="club-name">WKR Lindenmoos</span>
      </div>
      <svg class="town-band" role="img" aria-label="Ortssilhouette mit Kirchturm, Häusern und Baum in Grau" viewBox="0 0 590 36" preserveAspectRatio="none">
        <rect x="0" y="10" width="590" height="26" fill="var(--town-grey)"/>
      </svg>
      <div class="web-links">
        <span>www.wkr-lindenmoos.de</span>
        <span>www.lindenmoos-ort.de</span>
      </div>
    </footer>
  </main>
</body>
</html>
```